I am looking for a poster design with a pledge for my clients to take. The pledge will be to not use tanning beds. Our company is a Spray Tanning Salon that focuses on educating our clients on the dangers of indoor tanning while offering a safe alternative through spray tanning. I have an outline of a possible wording but I am VERY open to adjustments on it!
This is not a promotional poster. This is a poster that will be hanging in the salon and our clients will sign around the wall.
Updates

Project Deadline Extended Reason: Not currently in love with any submissions and would like to see more. Looking for a more simple design overall. Added Friday, October 28, 2016

Target Market(s)

Women 20-30 years old

Industry/Entity Type

Salon

Font styles to use
Sans Serif

Requirements
Must have
• Take the pledge to ditch the bed!
• Willowmere Tanning
• **Overall simple design, yet eye catching is requested. Not so busy**
Nice to have
• I am open to different wording!
• I pledge to be timeless
• -UVA rays in tanning beds cause wrinkles and other signs of premature aging
• I pledge to be fearless
• -Using tanning beds can cause severe eye damage, a weakened immune system, and melanoma the deadliest form of skin cancer.
• I pledge to be Sunless!
• -Join the LumaVeil revolution at Willowmere Tanning, Grand Rapids first Sunless Spa Experience.
Should not have
• The photo of the salon on it. I included that photo simply for reference of design, this is where this poster will be hung.

```html
<!DOCTYPE html>
<html lang="en">
<head>
<meta charset="utf-8">
<title>Willowmere Tanning – Spray Tanning Salon Pledge Poster</title>
<link href="https://fonts.googleapis.com/css2?family=Roboto+Condensed:ital,wght@0,300;0,400;0,700;1,400&display=swap" rel="stylesheet">
<style>
  :root {
    --sky-green: #58b36a;
    --sky-mid: #c9dfe9;
    --sky-blue: #9cc6e6;
    --ink: #111111;
    --white: #ffffff;
    --night: #111418;
    --accent-blue: #3b86c4;
    --sea-top: #2a9ec4;
    --sea-low: #4fb4cf;
    --skin: #c98a62;
    --sand: #cdb08c;
  }
  * { margin: 0; padding: 0; box-sizing: border-box; }
  html, body { width: 933px; height: 1200px; overflow: hidden; }
  body { font-family: "Roboto Condensed", "Arial Narrow", sans-serif; color: var(--ink); }

  .poster {
    position: relative;
    width: 933px;
    height: 1200px;
    overflow: hidden;
    background: linear-gradient(180deg, var(--sky-green) 0%, #a9d3b2 9%, var(--sky-mid) 20%, var(--sky-blue) 40%, #bcd9ea 56%);
  }

  .brand {
    position: absolute;
    top: 100px; left: 0; width: 100%;
    display: flex; justify-content: center; align-items: center; gap: 14px;
  }
  .brand-mark { width: 20px; height: 20px; background: var(--ink); }
  .brand-name { font-size: 44px; font-weight: 300; color: var(--ink); letter-spacing: 1px; line-height: 1; }

  .headline {
    position: absolute; top: 210px; width: 100%;
    text-align: center; font-size: 58px; font-weight: 400; line-height: 64px;
  }
  .intro {
    position: absolute; top: 282px; width: 100%;
    text-align: center; font-size: 20px; line-height: 24px; font-weight: 400;
  }

  .pledges { position: absolute; top: 350px; left: 0; width: 100%; }
  .pledge { position: absolute; width: 280px; text-align: center; }
  .pledge--timeless { left: 34px; }
  .pledge--fearless { left: 326px; }
  .pledge--sunless { left: 620px; }
  .pledge-icon { display: block; margin: 0 auto; width: 62px; height: 62px; }
  .pledge-title { font-style: italic; font-weight: 400; font-size: 31px; line-height: 36px; margin-top: 8px; }
  .pledge-text { font-size: 21px; line-height: 25px; margin-top: 14px; }

  .beach-photo {
    position: absolute; top: 676px; left: 0; width: 933px; height: 400px;
    background:
      linear-gradient(180deg, var(--sea-top) 0%, var(--sea-low) 30%, rgba(79,180,207,0) 45%),
      linear-gradient(180deg, var(--sea-low) 30%, var(--skin) 60%, var(--sand) 100%);
  }

  .pledge-call {
    position: absolute; top: 760px; width: 100%;
    text-align: center; font-size: 56px; font-weight: 700; line-height: 64px;
    color: var(--white); text-shadow: 0 2px 6px rgba(0,0,0,0.35);
  }

  .footer-band { position: absolute; top: 990px; left: 0; width: 933px; height: 210px; }

  .call-line {
    position: absolute; top: 1100px; width: 100%;
    text-align: center; font-size: 50px; font-weight: 400; line-height: 60px; color: var(--accent-blue);
    word-spacing: 4px;
  }
</style>
</head>
<body>
<main class="poster">
  <header class="brand">
    <span class="brand-mark"></span>
    <span class="brand-name">Willowmere Tanning</span>
  </header>

  <h1 class="headline">SPRAY TANNING SALON</h1>
  <p class="intro">Educating our clients on the dangers of indoor tanning while offering a<br>safe alternative through spray tanning.</p>

  <section class="pledges">
    <article class="pledge pledge--timeless">
      <svg class="pledge-icon" viewBox="0 0 70 70" aria-hidden="true">
        <circle cx="35" cy="35" r="31" fill="none" stroke="#fff" stroke-width="3"/>
        <path d="M35 14 V35 L26 46" fill="none" stroke="#fff" stroke-width="3" stroke-linecap="round"/>
      </svg>
      <h2 class="pledge-title">I pledge<br>to be timeless</h2>
      <p class="pledge-text">UVA rays in tanning<br>beds cause wrinkles<br>and other signs of<br>premature aging</p>
    </article>
    <article class="pledge pledge--fearless">
      <svg class="pledge-icon" viewBox="0 0 70 70" aria-hidden="true">
        <circle cx="35" cy="35" r="31" fill="none" stroke="#fff" stroke-width="3"/>
        <circle cx="25" cy="28" r="3.5" fill="#fff"/>
        <circle cx="45" cy="28" r="3.5" fill="#fff"/>
        <path d="M22 42 Q35 54 48 42" fill="none" stroke="#fff" stroke-width="3" stroke-linecap="round"/>
      </svg>
      <h2 class="pledge-title">I pledge<br>to be fearless</h2>
      <p class="pledge-text">Using tanning beds can<br>cause severe eye damage,<br>a weakened immune system,<br>and melanoma the deadliest<br>form of skin cancer.</p>
    </article>
    <article class="pledge pledge--sunless">
      <svg class="pledge-icon" viewBox="0 0 70 70" aria-hidden="true">
        <circle cx="35" cy="35" r="12" fill="#fff"/>
        <g stroke="#fff" stroke-width="3" stroke-linecap="round">
          <line x1="35" y1="4" x2="35" y2="17"/><line x1="35" y1="53" x2="35" y2="66"/>
          <line x1="4" y1="35" x2="17" y2="35"/><line x1="53" y1="35" x2="66" y2="35"/>
          <line x1="13" y1="13" x2="22" y2="22"/><line x1="48" y1="48" x2="57" y2="57"/>
          <line x1="57" y1="13" x2="48" y2="22"/><line x1="22" y1="48" x2="13" y2="57"/>
        </g>
      </svg>
      <h2 class="pledge-title">I pledge<br>to be Sunless!</h2>
      <p class="pledge-text">Using tanning beds can<br>cause severe eye damage,<br>a weakened immune<br>system, and melanoma<br>the deadliest form of<br>skin cancer.</p>
    </article>
  </section>

  <div class="beach-photo" role="img" aria-label="Photo of four friends sitting on the sand, seen from behind, looking out at a turquoise sea"></div>

  <h2 class="pledge-call">Take the pledge<br>to ditch the bed!</h2>

  <svg class="footer-band" viewBox="0 0 933 210" preserveAspectRatio="none" aria-hidden="true">
    <path d="M0 30 Q380 110 933 20 L933 210 L0 210 Z" fill="var(--accent-blue)"/>
    <path d="M0 30 Q380 112 933 38 L933 210 L0 210 Z" fill="var(--night)"/>
  </svg>

  <p class="call-line">Call Us Now&nbsp; 123456 7890</p>
</main>
</body>
</html>
```